Flyer for Aluminium recycling business

We are a startup aluminium recycling business. We don’t have a logo yet. I’ve attached a flyer created by one of our sales people but it’s a bit average and we need something a bit more modern and slick. You have creative license to completely change everything - as long as the information being communicated is the same.

Target Market(s)

Hospitality, Hotels, Apartment blocks, malls etcs

Industry/Entity Type

Aluminium recycling

Requirements
Must have
• the wording
Nice to have
• you have free license on design aspect

```html
<!DOCTYPE html>
<html lang="en">
<head>
<meta charset="utf-8">
<title>Cleanloop Metals – Aluminium Recycling Flyer</title>
<link href="https://fonts.googleapis.com/css2?family=Bebas+Neue&family=Poppins:wght@400;700&display=swap" rel="stylesheet">
<style>
  :root {
    --stage: #b6b6b8;
    --paper: #ffffff;
    --paper-shade: #f1f2f3;
    --green: #1fb04b;
    --ink: #111111;
    --metal-light: #d9dde2;
    --metal-dark: #6d737b;
    --sky: #c4d4e6;
  }
  * { margin: 0; padding: 0; box-sizing: border-box; }
  html, body { width: 982px; height: 1200px; overflow: hidden; background: var(--stage); }
  body { position: relative; font-family: "Poppins", sans-serif; color: var(--ink); }

  .flyer {
    position: absolute; left: 134px; top: 95px; width: 714px; height: 1010px;
    background: linear-gradient(160deg, var(--paper) 0%, var(--paper-shade) 55%, var(--paper) 100%);
    overflow: hidden;
  }
  .facets { position: absolute; inset: 0; }

  .hero-photo { position: absolute; left: 477px; top: -83px; width: 396px; height: 396px; }

  .headline {
    position: absolute; left: 44px; top: 44px;
    font-family: "Bebas Neue", sans-serif; font-size: 63px; line-height: 57px;
    letter-spacing: 0.2px; color: var(--ink);
  }
  .headline .accent { color: var(--green); }

  .bracket { position: absolute; left: 34px; top: 259px; width: 190px; height: 416px; }

  .section-title {
    position: absolute; left: 44px; top: 261px;
    font-weight: 700; font-size: 35px; line-height: 40px; color: var(--green); letter-spacing: 0.3px;
  }
  .subhead {
    position: absolute; left: 44px; font-weight: 700; font-size: 15px; line-height: 18px;
  }
  .subhead.simple { top: 314px; }
  .subhead.examples { top: 533px; }

  .ticks { position: absolute; left: 44px; list-style: none; font-size: 13.6px; line-height: 17.5px; }
  .ticks li { position: relative; padding-left: 17px; }
  .ticks li svg { position: absolute; left: 0; top: 3px; width: 12px; height: 12px; }
  .ticks.steps { top: 353px; }
  .ticks.steps li { margin-bottom: 7px; }
  .ticks.items { top: 565px; }
  .ticks.items li { margin-bottom: 4.5px; }

  .gallery { position: absolute; left: 42px; top: 705px; width: 630px; height: 210px; }
  .gallery .shot { position: absolute; top: 0; width: 188px; height: 188px; border-radius: 50%;
    border: 7px solid var(--green); overflow: hidden; }
  .gallery .shadow { position: absolute; top: 188px; width: 150px; height: 14px; border-radius: 50%;
    background: radial-gradient(ellipse at center, rgba(0,0,0,0.22), rgba(0,0,0,0) 70%); }
  .shot.scrap { left: 0; background: linear-gradient(180deg, #4d77b0 0%, #8f939a 35%, #5b5f66 100%); }
  .shot.cans { left: 147px; background: radial-gradient(circle at 40% 40%, #d8d9d2, #b9b5a0 45%, #7f8f6e 100%); }
  .shot.trays { left: 295px; background: radial-gradient(circle at 50% 55%, #cfd2d6 0%, #eef0f2 45%, #ffffff 70%); }
  .shot.caps { left: 442px; background: linear-gradient(135deg, #d8d8dc 0%, #e07a48 35%, #3aa36b 60%, #d1467a 85%, #3242a3 100%); }

  .cta { position: absolute; left: 44px; top: 932px; font-weight: 700; font-size: 27px; line-height: 32px; color: var(--green); letter-spacing: 0.2px; }
  .email { position: absolute; left: 44px; top: 965px; font-size: 14px; line-height: 18px; }

  .brand { position: absolute; left: 475px; top: 932px; display: flex; align-items: center; gap: 10px; }
  .brand .mark { width: 40px; height: 40px; border-radius: 50%; background: var(--green); }
  .brand .name { font-weight: 700; font-size: 19.5px; line-height: 20px; color: var(--ink); letter-spacing: 0.3px; }
</style>
</head>
<body>
  <main class="flyer">
    <svg class="facets" viewBox="0 0 714 1010" aria-hidden="true">
      <polygon points="0,250 160,0 420,0" fill="#ffffff" opacity="0.7"/>
      <polygon points="0,250 420,0 520,430" fill="#eef0f2" opacity="0.5"/>
      <polygon points="520,430 714,300 714,780" fill="#f6f7f8"/>
      <polygon points="420,840 714,600 714,1010" fill="#eceef0" opacity="0.6"/>
      <line x1="0" y1="22" x2="40" y2="0" stroke="#ffffff" stroke-width="2"/>
    </svg>

    <svg class="hero-photo" viewBox="0 0 396 396" role="img" aria-label="Photo of a heap of shredded aluminium scrap under a pale sky">
      <defs>
        <linearGradient id="scrap-sky" x1="0" y1="0" x2="0" y2="1">
          <stop offset="0" stop-color="var(--sky)"/>
          <stop offset="0.45" stop-color="#dfe6ee"/>
          <stop offset="0.55" stop-color="#9aa1a9"/>
          <stop offset="1" stop-color="#5f656d"/>
        </linearGradient>
      </defs>
      <circle cx="198" cy="198" r="193" fill="var(--green)"/>
      <circle cx="198" cy="198" r="183" fill="url(#scrap-sky)"/>
    </svg>

    <h1 class="headline">
      <span>PLAYING THE FAIR</span><br>
      <span class="accent">ALUMINIUM RECYCLING</span><br>
      <span>GAME FOR GOOD</span>
    </h1>

    <svg class="bracket" viewBox="0 0 190 416" aria-hidden="true">
      <path d="M1 416 V14 Q1 1 14 1 H190" fill="none" stroke="var(--green)" stroke-width="1.3"/>
    </svg>

    <h2 class="section-title">YOU ARE HERE</h2>

    <h3 class="subhead simple">IT'S SIMPLE:</h3>
    <ul class="ticks steps">
      <li><svg viewBox="0 0 12 12"><circle cx="6" cy="6" r="5" fill="none" stroke="var(--green)" stroke-width="1.3"/><path d="M3.3 6.2 5.3 8.1 10.5 2.4" fill="none" stroke="var(--green)" stroke-width="1.5" stroke-linecap="round"/></svg>We bring you a free bin</li>
      <li><svg viewBox="0 0 12 12"><circle cx="6" cy="6" r="5" fill="none" stroke="var(--green)" stroke-width="1.3"/><path d="M3.3 6.2 5.3 8.1 10.5 2.4" fill="none" stroke="var(--green)" stroke-width="1.5" stroke-linecap="round"/></svg>You throw all and any aluminium waste into the bin - no need to super-clean it. Try<br>to compact / squash the aluminium as much as possible</li>
      <li><svg viewBox="0 0 12 12"><circle cx="6" cy="6" r="5" fill="none" stroke="var(--green)" stroke-width="1.3"/><path d="M3.3 6.2 5.3 8.1 10.5 2.4" fill="none" stroke="var(--green)" stroke-width="1.5" stroke-linecap="round"/></svg>We collect the bin at no charge</li>
      <li><svg viewBox="0 0 12 12"><circle cx="6" cy="6" r="5" fill="none" stroke="var(--green)" stroke-width="1.3"/><path d="M3.3 6.2 5.3 8.1 10.5 2.4" fill="none" stroke="var(--green)" stroke-width="1.5" stroke-linecap="round"/></svg>We turn the aluminium waste into a desirable resource</li>
      <li><svg viewBox="0 0 12 12"><circle cx="6" cy="6" r="5" fill="none" stroke="var(--green)" stroke-width="1.3"/><path d="M3.3 6.2 5.3 8.1 10.5 2.4" fill="none" stroke="var(--green)" stroke-width="1.5" stroke-linecap="round"/></svg>We pay you for however much of that resource your waste has generated - and give<br>you a report on that, so you can see how good you are</li>
    </ul>

    <h3 class="subhead examples">EXAMPLES OF WHAT WE CAN TAKE:</h3>
    <ul class="ticks items">
      <li><svg viewBox="0 0 12 12"><circle cx="6" cy="6" r="5" fill="none" stroke="var(--green)" stroke-width="1.3"/><path d="M3.3 6.2 5.3 8.1 10.5 2.4" fill="none" stroke="var(--green)" stroke-width="1.5" stroke-linecap="round"/></svg>Used beverage cans - any</li>
      <li><svg viewBox="0 0 12 12"><circle cx="6" cy="6" r="5" fill="none" stroke="var(--green)" stroke-width="1.3"/><path d="M3.3 6.2 5.3 8.1 10.5 2.4" fill="none" stroke="var(--green)" stroke-width="1.5" stroke-linecap="round"/></svg>Tinfoil-scrunched, crusty, burned or dirty</li>
      <li><svg viewBox="0 0 12 12"><circle cx="6" cy="6" r="5" fill="none" stroke="var(--green)" stroke-width="1.3"/><path d="M3.3 6.2 5.3 8.1 10.5 2.4" fill="none" stroke="var(--green)" stroke-width="1.5" stroke-linecap="round"/></svg>Disposable BBQ roasting trays</li>
      <li><svg viewBox="0 0 12 12"><circle cx="6" cy="6" r="5" fill="none" stroke="var(--green)" stroke-width="1.3"/><path d="M3.3 6.2 5.3 8.1 10.5 2.4" fill="none" stroke="var(--green)" stroke-width="1.5" stroke-linecap="round"/></svg>Aluminium takeaway containers</li>
      <li><svg viewBox="0 0 12 12"><circle cx="6" cy="6" r="5" fill="none" stroke="var(--green)" stroke-width="1.3"/><path d="M3.3 6.2 5.3 8.1 10.5 2.4" fill="none" stroke="var(--green)" stroke-width="1.5" stroke-linecap="round"/></svg>Wine bottle screw tops (and collars - if you can get them off)</li>
    </ul>

    <section class="gallery">
      <span class="shadow" style="left:19px"></span>
      <span class="shadow" style="left:166px"></span>
      <span class="shadow" style="left:314px"></span>
      <span class="shadow" style="left:461px"></span>
      <div class="shot scrap" role="img" aria-label="Photo of baled aluminium scrap stacked outdoors"></div>
      <div class="shot cans" role="img" aria-label="Photo of crushed used beverage cans"></div>
      <div class="shot trays" role="img" aria-label="Photo of disposable aluminium BBQ roasting trays"></div>
      <div class="shot caps" role="img" aria-label="Photo of colourful aluminium wine bottle screw caps"></div>
    </section>

    <p class="cta">CALL NOW! 026 555 0148</p>
    <p class="email">join@cleanloopmetals.co.nz</p>

    <div class="brand">
      <span class="mark" aria-hidden="true"></span>
      <span class="name">CLEANLOOP<br>METALS</span>
    </div>
  </main>
</body>
</html>
```